Purpose, Mission, and Values Poster Update

Bridgewell Quality Labs, a Testing, Inspection, and Certification company in the Atlanta area, needs an updated PMV poster. Looking to update graphics and presentation, moving away from current design. Want to carry over company logo, colors (you can include additional blues in the design beyond what is mentioned in the brand guidelines as the previous design did), and messaging (see attachments).

We would also like a companion poster, using the same design language, that shows our goals for leads and won opportunities. Want to carry over logo, colors, and messaging from original, except for this one we want the leads goal to be 115 instead of 85.

Both posters need to be 6000w x 7200h at 300ppi, CMYK. We want to move away from the cartoony, corporate clipart sort of look that the current design has, as new leadership doesn't like the aesthetic.

Target Market(s)

Internal - group of engineers, chemists, scientists, and other technical personnel

Industry/Entity Type

TIC (Testing, Inspection, Certification)

Font styles to use
Serif
Sans Serif

Colors
0054AA
0677BA
7BADD7
CADEEF
E8F1F8

Requirements
Must have
• For both: CMYK colors for printing, 6000w x 7200h at 300ppi for poster sizing leads, company logo; for PMV poster: phrasing of purpose, mission, and values statements preserved; for ring the bell poster: leads goal updated to 115, opportunities goal unchanged at 25
Should not have
• Corporate clipart, cartoon characters

```html
<!DOCTYPE html>
<html lang="en">
<head>
<meta charset="utf-8">
<title>Bridgewell Quality Labs – Purpose, Mission, Values and Ring the Bell Posters</title>
<link rel="stylesheet" href="https://fonts.googleapis.com/css2?family=Bebas+Neue&family=Montserrat:wght@600;700;800&family=Roboto+Condensed:wght@300;400&display=swap">
<style>
  :root{
    --blue-bright:#0a5fe0;
    --blue-mid:#0a4fc4;
    --blue-deep:#0a3c9e;
    --navy:#0b4a7a;
    --line-blue:#1f5a99;
    --paper-top:#ffffff;
    --paper-bottom:#e9eaeb;
    --ink:#2a2a2a;
    --stage:#e4e5e6;
    --white:#ffffff;
    --photo-dark:#2e2f31;
    --photo-light:#9a9b9d;
  }
  *{margin:0;padding:0;box-sizing:border-box}
  html,body{width:1200px;height:693px;overflow:hidden;background:var(--stage)}
  .canvas{position:relative;width:1200px;height:693px}
  .poster{position:absolute;top:53px;width:472px;height:567px;overflow:hidden;
    background:linear-gradient(180deg,var(--paper-top),var(--paper-bottom));
    box-shadow:0 10px 18px rgba(0,0,0,.18)}
  .poster--pmv{left:57px}
  .poster--bell{left:670px}
  .blue-field{position:absolute;left:0;top:0;width:100%;
    background:linear-gradient(180deg,var(--blue-bright) 0%,var(--blue-mid) 55%,var(--blue-deep) 100%)}
  .poster--pmv .blue-field{height:265px}
  .poster--bell .blue-field{height:410px}
  .photo{position:absolute;left:0;width:100%;opacity:.82;
    background:linear-gradient(90deg,var(--photo-dark) 0%,#48494b 28%,var(--photo-light) 50%,#48494b 72%,var(--photo-dark) 100%);
    -webkit-mask-image:linear-gradient(180deg,transparent 0%,#000 30%,#000 62%,transparent 100%);
    mask-image:linear-gradient(180deg,transparent 0%,#000 30%,#000 62%,transparent 100%)}
  .poster--pmv .photo{top:140px;height:180px}
  .poster--bell .photo{top:310px;height:190px}
  .rules{position:absolute;left:0;top:0;width:472px;height:567px;pointer-events:none}
  .icon{position:absolute}
  .wordmark{position:absolute;left:0;width:100%;font-family:'Montserrat',sans-serif;font-weight:700;text-align:center;white-space:nowrap}
  .poster--pmv .wordmark{top:46px;font-size:10.5px;color:var(--white)}
  .poster--bell .wordmark{top:525px;font-size:11px;color:#111}
  .statement{position:absolute;color:var(--white)}
  .statement h2{font-family:'Bebas Neue',sans-serif;font-weight:400;font-size:30px;line-height:23px}
  .statement p{font-family:'Roboto Condensed',sans-serif;font-weight:300;font-size:12px;line-height:12.6px;margin-top:5px}
  .statement--purpose{left:111px;top:66px}
  .statement--mission{right:97px;top:66px;text-align:right}
  .values-title{position:absolute;left:0;width:100%;top:318px;text-align:center;line-height:1;
    font-family:'Bebas Neue',sans-serif;font-weight:400;font-size:28px;letter-spacing:5px;color:var(--navy)}
  .value{position:absolute;text-align:center;color:var(--navy)}
  .value svg{display:block;margin:0 auto}
  .value h3{font-family:'Montserrat',sans-serif;font-weight:600;font-size:11px;line-height:12.2px}
  .value p{font-family:'Roboto Condensed',sans-serif;font-weight:300;font-size:7.8px;line-height:8.2px;color:var(--ink);margin-top:9px}
  .faint-name{margin-top:12px;font-family:'Montserrat',sans-serif;font-weight:600;font-size:6.5px;color:#c4c8cc}
  .kicker{position:absolute;left:0;width:100%;text-align:center;color:var(--white);line-height:1.1}
  .kicker--light{font-family:'Roboto Condensed',sans-serif;font-weight:300;font-size:19px}
  .kicker--bold{font-family:'Montserrat',sans-serif;font-weight:700;font-size:21px}
  .ring-title{position:absolute;left:96px;top:146px;display:flex;align-items:baseline;color:var(--white)}
  .ring-title .big{font-family:'Montserrat',sans-serif;font-weight:800;font-size:57px;line-height:1;letter-spacing:-1px}
  .ring-title .small{font-family:'Bebas Neue',sans-serif;font-size:31px;line-height:1;margin:0 4px}
  .ring-title .we{position:absolute;left:57px;top:-14px;font-family:'Bebas Neue',sans-serif;font-size:30px;line-height:1}
</style>
</head>
<body>
<main class="canvas">

  <!-- Purpose, Mission & Values poster -->
  <section class="poster poster--pmv">
    <div class="blue-field"></div>
    <div class="photo" role="img" aria-label="Black and white photo of two businessmen in suits shaking hands"></div>

    <svg class="rules" viewBox="0 0 472 567" aria-hidden="true">
      <g fill="none" stroke="rgba(255,255,255,.75)" stroke-width="1">
        <polyline points="0,43 158,43 168,55"/>
        <polyline points="472,43 314,43 304,55"/>
        <polyline points="205,78 221,94 221,180"/>
        <polyline points="268,78 251,94 251,180"/>
      </g>
      <g fill="none" stroke="var(--line-blue)" stroke-width="1">
        <polyline points="43,258 43,349"/>
        <polyline points="433,258 433,349"/>
        <polyline points="74,511 94,532 382,532 402,511"/>
      </g>
      <g fill="#fff" stroke="var(--line-blue)" stroke-width="1" style="filter:drop-shadow(0 4px 4px rgba(0,0,0,.18))">
        <path d="M33,351 L102,365 L102,504 L33,516 Q25,517 25,509 V358 Q25,350 33,351Z"/>
        <path d="M111,349 L182,365 L182,504 L111,516 Q103,517 103,509 V356 Q103,348 111,349Z"/>
        <path d="M365,349 L285,365 L285,504 L365,516 Q373,517 373,509 V356 Q373,348 365,349Z"/>
        <path d="M443,351 L373,365 L373,504 L443,516 Q451,517 451,509 V358 Q451,350 443,351Z"/>
        <rect x="182" y="354" width="103" height="160" rx="12"/>
      </g>
    </svg>

    <div class="wordmark">Bridgewell Quality Labs</div>

    <svg class="icon" style="left:26px;top:60px" width="70" height="68" viewBox="0 0 70 68" fill="none" stroke="#fff" stroke-width="2" stroke-linejoin="round" stroke-linecap="round" aria-hidden="true">
      <path d="M6,6 Q20,1 30,5 Q40,1 50,6 V28 Q50,46 28,58 Q6,46 6,28Z"/>
      <circle cx="21" cy="24" r="11"/>
      <ellipse cx="21" cy="24" rx="5" ry="11"/>
      <line x1="10" y1="24" x2="32" y2="24"/>
      <circle cx="48" cy="34" r="13" fill="#0a55d0"/>
      <path d="M43,29 L48,27 L53,29 V34 Q53,38 48,41 Q43,38 43,34Z"/>
      <line x1="52" y1="46" x2="57" y2="63" stroke-width="3.5"/>
    </svg>
    <div class="statement statement--purpose">
      <h2>Our<br>Purpose</h2>
      <p>Create a safe<br>And reliable<br>World</p>
    </div>

    <svg class="icon" style="left:392px;top:58px" width="58" height="70" viewBox="0 0 58 70" fill="none" stroke="#fff" stroke-width="2" stroke-linejoin="round" stroke-linecap="round" aria-hidden="true">
      <circle cx="26" cy="30" r="17"/>
      <circle cx="26" cy="30" r="10"/>
      <circle cx="26" cy="30" r="3.5"/>
      <line x1="26" y1="30" x2="50" y2="6"/>
      <polyline points="43,5 50,6 51,13"/>
      <path d="M4,30 V48 Q4,56 12,60 L18,64 V68 M48,30 V48 Q48,56 40,60 L34,64 V68"/>
    </svg>
    <div class="statement statement--mission">
      <h2>Our<br>Mission</h2>
      <p>Deliver assurance<br>through Precise<br>technical and<br>Professional services</p>
    </div>

    <h2 class="values-title">OUR VALUES</h2>

    <div class="value" style="left:27px;width:73px;top:366px">
      <svg width="40" height="40" viewBox="0 0 40 40" fill="none" stroke="var(--navy)" stroke-width="1.4" stroke-linecap="round" stroke-linejoin="round" aria-hidden="true">
        <circle cx="12" cy="7" r="3"/><circle cx="20" cy="5" r="3"/><circle cx="28" cy="7" r="3"/>
        <path d="M13,22 Q13,13 20,13 Q27,13 27,22Z"/>
        <path d="M4,28 Q10,26 16,29 H24 Q28,29 24,32 H16 M4,34 Q14,38 24,36 L36,28 Q37,25 33,26 L26,30"/>
      </svg>
      <h3 style="margin-top:6px">Keep<br>People<br>First</h3>
      <p style="margin-top:8px">Foster a<br>collaborative<br>&amp; inclusive<br>environment for team<br>members' growth</p>
    </div>
    <div class="value" style="left:105px;width:75px;top:366px">
      <svg width="40" height="40" viewBox="0 0 40 40" fill="none" stroke="var(--navy)" stroke-width="1.4" stroke-linecap="round" stroke-linejoin="round" aria-hidden="true">
        <path d="M19,6 H31 L35,11 L25,23 L15,11Z"/><path d="M15,11 H35 M22,6 L25,23 L28,6"/>
        <path d="M25,1 V3 M19,2 L20,4 M31,2 L30,4"/>
        <path d="M3,30 Q10,27 16,30 H23 Q27,30 23,33 H16 M5,36 Q15,39 24,37 L36,29 Q37,26 33,27 L26,31"/>
      </svg>
      <h3 style="margin-top:10px">Deliver<br>Service<br>Excellence</h3>
      <p>Provide<br>best-in-class<br>experience<br>for our clients</p>
    </div>
    <div class="value" style="left:184px;width:99px;top:362px">
      <svg width="44" height="46" viewBox="0 0 44 46" fill="none" stroke="var(--navy)" stroke-width="1.4" stroke-linecap="round" stroke-linejoin="round" aria-hidden="true">
        <circle cx="22" cy="19" r="13"/>
        <ellipse cx="22" cy="19" rx="6" ry="13"/>
        <line x1="9" y1="19" x2="35" y2="19"/>
        <path d="M16,32 V37 H28 V32 M16,40 H28 M18,43 H26"/>
        <path d="M22,1 V3 M5,19 H3 M39,19 H41 M9,6 L11,8 M35,6 L33,8"/>
      </svg>
      <h3 style="margin-top:6px">Think Global,<br>Act Local</h3>
      <p style="margin-top:6px">Utilize our combined<br>expertise &amp; knowledge to<br>deliver when and where</p>
      <div class="faint-name">Bridgewell Quality Labs</div>
    </div>
    <div class="value" style="left:287px;width:84px;top:366px">
      <svg width="42" height="44" viewBox="0 0 42 44" fill="none" stroke="var(--navy)" stroke-width="1.4" stroke-linecap="round" stroke-linejoin="round" aria-hidden="true">
        <path d="M21,2 L23,7 L28,7 L24,10 L26,15 L21,12 L16,15 L18,10 L14,7 L19,7Z"/>
        <path d="M7,12 L9,16 L13,16 L10,19 L11,23 L7,21 L3,23 L4,19 L1,16 L5,16Z"/>
        <path d="M35,12 L37,16 L41,16 L38,19 L39,23 L35,21 L31,23 L32,19 L29,16 L33,16Z"/>
        <circle cx="19" cy="26" r="5"/>
        <path d="M9,42 Q9,32 19,32 Q24,32 26,35"/>
        <circle cx="30" cy="38" r="5"/><polyline points="27.5,38 29.5,40 32.5,36"/>
      </svg>
      <h3 style="margin-top:6px">Create<br>Value</h3>
      <p>Work efficiently and<br>effectively to deliver<br>quality results in a<br>complex environments</p>
    </div>
    <div class="value" style="left:375px;width:75px;top:366px">
      <svg width="42" height="42" viewBox="0 0 42 42" fill="none" stroke="var(--navy)" stroke-width="1.4" stroke-linecap="round" stroke-linejoin="round" aria-hidden="true">
        <line x1="3" y1="6" x2="39" y2="6"/>
        <rect x="17" y="2" width="8" height="8" rx="2"/>
        <line x1="21" y1="10" x2="21" y2="37"/>
        <path d="M9,6 L4,22 H14Z M33,6 L28,22 H38Z"/>
        <path d="M4,22 Q9,27 14,22 M28,22 Q33,27 38,22"/>
        <path d="M13,37 H29 M3,40 H39"/>
      </svg>
      <h3 style="margin-top:8px">Do What's<br>Right</h3>
      <p>Hold ourselves<br>accountable to the<br>highest safety,<br>professional and<br>personal standards</p>
    </div>
  </section>

  <!-- Ring the Bell poster -->
  <section class="poster poster--bell">
    <div class="blue-field"></div>
    <div class="photo" role="img" aria-label="Black and white photo of two businessmen in suits shaking hands"></div>

    <svg class="rules" viewBox="0 0 472 567" aria-hidden="true">
      <path d="M181,121 H86 Q80,121 80,127 V212 Q80,218 86,218 H396 Q402,218 402,212 V127 Q402,121 396,121 H290"
            fill="none" stroke="rgba(255,255,255,.8)" stroke-width="0.8" stroke-dasharray="2 1.6"/>
      <g fill="none" stroke="rgba(255,255,255,.45)" stroke-width="1">
        <line x1="44" y1="232" x2="44" y2="360"/>
        <line x1="433" y1="232" x2="433" y2="360"/>
      </g>
      <g fill="none" stroke="var(--line-blue)" stroke-width="1">
        <polyline points="44,470 44,482 94,532 179,532"/>
        <polyline points="433,470 433,482 382,532 289,532"/>
      </g>
    </svg>

    <div class="kicker kicker--light" style="top:31px">Celebrating Our Opportunities to</div>
    <div class="kicker kicker--bold" style="top:52px;font-size:18.5px">Create a Safe and Reliable World</div>

    <svg class="icon" style="left:191px;top:85px" width="90" height="72" viewBox="0 0 90 72" fill="none" stroke="#fff" stroke-width="2.6" stroke-linecap="round" stroke-linejoin="round" aria-hidden="true">
      <circle cx="45" cy="5" r="3"/>
      <path d="M45,8 Q30,8 28,26 Q26,44 18,54 H72 Q64,44 62,26 Q60,8 45,8Z"/>
      <path d="M14,54 Q10,60 18,62 H72 Q80,60 76,54"/>
      <path d="M38,62 Q38,70 45,70 Q52,70 52,62"/>
      <path d="M14,22 Q8,30 14,38 M7,17 Q-1,30 7,43 M76,22 Q82,30 76,38 M83,17 Q91,30 83,43"/>
    </svg>

    <div class="ring-title">
      <span class="we">WE</span>
      <span class="big">Ring</span><span class="small">THE</span><span class="big">Bell</span>
    </div>

    <div class="kicker kicker--light" style="top:234px;font-size:20px">Once when we've hit</div>
    <div class="kicker kicker--bold" style="top:256px">115 LEADS</div>
    <div class="kicker kicker--light" style="top:287px;font-size:20px">Twice when we've won</div>
    <div class="kicker kicker--bold" style="top:309px">25 OPPORTUNITIES</div>

    <div class="wordmark">Bridgewell Quality Labs</div>
  </section>

</main>
</body>
</html>
```